Urgent flyer/ brochure design for NGO in one day

Hi - need help with NGO's brochure/ flyer design. It needs to be done in one day please. Would prefer that the overall document is A4, whether its a single flyer with two sided design or content, or whether you make trifold, is your choice.
Attached is ppt with content, the logo, the brand patterns, photos to be used etc.
We are keen on having a collage of the women's photos in some way in the design.
Pls do not upload just templates or random images, winner will be decided only amongst those who upload the completely made brochure/ flyer.
If a good design is submitted, award will be given. We have had some very bad entries in the past and lost money so not guaranteed contest yet. As NGO we cant afford to lose money. Final files will be needed as pdf and AI/ CDR, not photoshop.

```html
<!DOCTYPE html>
<html lang="en">
<head>
<meta charset="utf-8">
<title>Sangini Vatika – Brochure</title>
<link href="https://fonts.googleapis.com/css2?family=Barlow:wght@400;500;600;700&family=Hind:wght@500&display=swap" rel="stylesheet">
<style>
:root{
  --bg:#ececec;
  --paper:#ffffff;
  --orange:#f7a823;
  --indigo:#302d8a;
  --teal:#25a08b;
  --teal-dark:#14857a;
  --lime:#bfd22f;
  --lime-pale:#eef3cc;
  --ink:#3a3a3a;
  --muted:#6c6c6c;
}
*{box-sizing:border-box;margin:0;padding:0}
html,body{width:841px;height:1200px;overflow:hidden;background:var(--bg)}
body{font-family:"Barlow",Arial,sans-serif;color:var(--ink);position:relative}
.sheet{position:absolute;left:53px;width:735px;background:var(--paper);box-shadow:0 4px 10px rgba(0,0,0,.22);display:flex;overflow:hidden}
.sheet--outside{top:54px;height:520px}
.sheet--inside{top:618px;height:522px}
h2{font-weight:700;font-size:14px;letter-spacing:.3px;text-transform:uppercase;line-height:1.1}
p,li{font-size:7.6px;line-height:1.45}
ul{list-style:none}
.ticks li{position:relative;padding-left:18px;margin-bottom:7px}
.ticks li::before{content:"";position:absolute;left:3px;top:2px;border-left:3.5px solid transparent;border-right:3.5px solid transparent;border-top:6px solid var(--tick,var(--orange))}
.ticks ul{margin-top:6px}
.ticks ul li{padding-left:14px;margin-bottom:5px}
.ticks ul li::before{border-left-width:2.5px;border-right-width:2.5px;border-top-width:4.5px;opacity:.7}
.rule{border:0;border-top:1px dotted #999;margin:12px 0}
.rule--solid{border-top:1px solid #bbb}

/* outside */
.cover-left{width:246px;display:flex;flex-direction:column}
.cover-left .body{padding:16px 20px 0 22px}
.cover-left h2{color:var(--orange);margin-bottom:7px}
.word-pair{display:flex;gap:0;margin-bottom:10px}
.word{flex:1;font-size:7.6px;line-height:1.35}
.word + .word{border-left:1px dotted #999;padding-left:14px;margin-left:4px}
.word .deva{font-family:"Hind",sans-serif;font-size:8px;display:block;margin-bottom:5px}
.cover-right{flex:1;display:flex;flex-direction:column}
.quote-band{height:77px;background:var(--orange);position:relative;padding:16px 150px 0 40px}
.quote-band p{font-size:10px;line-height:1.4;color:#2b2b2b}
.quote-band .mark{position:absolute;font-size:30px;font-weight:700;color:#c0392b;line-height:1}
.quote-band .open{left:16px;top:8px}
.quote-band .close{left:222px;top:44px}
.brand-band{flex:1;background:var(--indigo);display:flex;justify-content:space-between;padding:24px 30px 0 46px}
.contacts li{display:flex;align-items:center;gap:10px;font-size:10.5px;color:var(--orange);margin-bottom:16px}
.contacts svg{flex:none}
.brand{width:170px;text-align:center}
.brand-name{display:flex;align-items:center;justify-content:center;gap:7px;font-size:18px;font-weight:700;color:var(--orange);margin-top:-6px;margin-bottom:12px}
.brand-name i{width:14px;height:14px;border-radius:50%;background:var(--orange)}
.tagline{font-size:14.5px;font-weight:600;line-height:1.2;color:var(--orange);text-transform:uppercase}

/* inside */
.panel{width:245px;padding:20px 18px 0 20px;position:relative}
.panel--why{border-left:7px solid var(--lime);padding-left:14px}
.panel--where{background:var(--teal);color:#fff;--tick:var(--lime)}
.panel--how{border-right:7px solid var(--teal);padding-right:18px}
.panel--how::after{content:"";position:absolute;right:-7px;top:340px;width:7px;height:182px;background:var(--orange)}
.panel--how::before{content:"";position:absolute;right:-7px;top:170px;width:7px;height:170px;background:var(--lime)}
.panel--why h2.lime{color:var(--lime)}
.subhead{text-align:center;color:var(--lime);font-size:10px;font-weight:600;margin:12px 0 10px}
.stats{display:grid;grid-template-columns:1fr 1fr;gap:8px 10px;justify-items:center}
.stat{position:relative;width:90px;height:90px}
.stat svg{position:absolute;inset:0}
.stat p{position:absolute;inset:22px 12px;display:flex;align-items:center;justify-content:center;text-align:center;font-size:6.4px;line-height:1.3}
.stat-box{width:96px;align-self:center;border:1px dashed var(--lime);padding:6px;font-size:6.4px;line-height:1.35;margin-top:14px}
.panel--why .ticks,.panel--how .ticks{--tick:var(--teal)}
.panel--why h2.teal{color:var(--teal-dark);margin-bottom:12px}
.panel--where h2{color:var(--lime);margin:10px 0 12px}
.panel--where li{font-size:7.4px;margin-bottom:12px}
.panel--where .rule{border-top-color:rgba(255,255,255,.55);margin:4px 0 14px}
.panel--how h2{color:var(--teal-dark);margin:10px 0 12px}
.panel--how h2.orange{color:var(--orange)}
.panel--how .help{--tick:var(--orange)}
.panel--how .help li{margin-bottom:9px}
.panel--how li{margin-bottom:12px}
</style>
</head>
<body>

<section class="sheet sheet--outside">
  <div class="cover-left">
    <svg class="collage" width="246" height="206" viewBox="0 0 246 206" role="img" aria-label="Collage of photos of beaded craftwork, a fabric box and painted folk artwork of women">
      <rect width="246" height="206" fill="#d9cbbf"/>
      <polygon points="0,0 128,0 128,180 0,206" fill="#b8a99c"/>
      <polygon points="128,0 246,0 246,125 128,120" fill="#d78a6a"/>
      <polygon points="0,130 128,110 128,206 0,206" fill="#a6302f"/>
      <polygon points="128,120 246,125 246,206 128,206" fill="#c9c6b4"/>
      <polyline points="0,0 128,110 246,206" stroke="#fff" stroke-width="3" fill="none"/>
      <line x1="128" y1="0" x2="128" y2="206" stroke="#fff" stroke-width="3"/>
      <line x1="128" y1="120" x2="246" y2="125" stroke="#fff" stroke-width="3"/>
    </svg>
    <div class="body">
      <h2>Who are we?</h2>
      <div class="word-pair">
        <div class="word"><span class="deva">संगिनी</span>a Hindi word that means “a female companion” in English.</div>
        <div class="word"><span class="deva">वाटिका</span>a Hindi word that means “a small garden” in English.</div>
      </div>
      <p>Sangini Vatika is a registered society under the Delhi government, working together to empower themselves and help other unprivileged women.</p>
      <hr class="rule">
      <h2>Our commitment</h2>
      <ul class="ticks">
        <li>Empower women, both economically and socially, by enhancing their self-esteem.</li>
        <li>Make the artisan members:
          <ul>
            <li>self-sustainable women with access and control over significant financial and social resources</li>
            <li>Uplift their status in their family and society.</li>
          </ul>
        </li>
      </ul>
    </div>
  </div>
  <div class="cover-right">
    <svg class="collage" width="489" height="327" viewBox="0 0 489 327" role="img" aria-label="Collage of painted folk art of village women and photos of the artisan women at work">
      <rect width="489" height="327" fill="#d5a38a"/>
      <polygon points="0,0 135,0 135,327 0,327" fill="#4d8a5a"/>
      <polygon points="135,0 260,0 260,170 135,190" fill="#7fb7c9"/>
      <polygon points="135,190 260,170 260,327 135,327" fill="#c8485a"/>
      <polygon points="260,0 489,0 489,60 260,130" fill="#d7c6b8"/>
      <polygon points="260,130 489,60 489,200 260,230" fill="#b26a5a"/>
      <polygon points="260,230 489,200 489,327 260,327" fill="#c36b88"/>
      <g stroke="#fff" stroke-width="3" fill="none">
        <line x1="135" y1="0" x2="135" y2="327"/>
        <line x1="260" y1="0" x2="260" y2="327"/>
        <line x1="135" y1="190" x2="260" y2="170"/>
        <line x1="260" y1="130" x2="489" y2="60"/>
        <line x1="260" y1="230" x2="489" y2="200"/>
        <line x1="0" y1="60" x2="135" y2="250"/>
        <line x1="340" y1="0" x2="420" y2="327"/>
      </g>
    </svg>
    <div class="quote-band">
      <span class="mark open">“</span>
      <p>A successful woman is one who can build a firm foundation with the bricks others have thrown at her.</p>
      <span class="mark close">”</span>
    </div>
    <div class="brand-band">
      <ul class="contacts">
        <li>
          <svg width="22" height="22" viewBox="0 0 22 22"><circle cx="11" cy="11" r="10" fill="none" stroke="#f7a823" stroke-width="1.2"/><rect x="5.5" y="7" width="11" height="8" fill="none" stroke="#f7a823" stroke-width="1.1"/><polyline points="5.5,7 11,11.5 16.5,7" fill="none" stroke="#f7a823" stroke-width="1.1"/></svg>
          contact@sanginivatika.org
        </li>
        <li>
          <svg width="22" height="22" viewBox="0 0 22 22"><circle cx="11" cy="11" r="10" fill="none" stroke="#f7a823" stroke-width="1.2"/><circle cx="11" cy="11" r="5.5" fill="none" stroke="#f7a823" stroke-width="1.1"/><line x1="5.5" y1="11" x2="16.5" y2="11" stroke="#f7a823"/><ellipse cx="11" cy="11" rx="2.3" ry="5.5" fill="none" stroke="#f7a823"/></svg>
          www.sanginivatika.org
        </li>
      </ul>
      <div class="brand">
        <div class="brand-name"><i></i>Sangini Vatika</div>
        <p class="tagline">Enriching the lives of women by empowering them</p>
      </div>
    </div>
  </div>
</section>

<section class="sheet sheet--inside">
  <div class="panel panel--why">
    <h2 class="lime">Why women empowerment?</h2>
    <p class="subhead">Women as Workers:</p>
    <div class="stats">
      <div class="stat">
        <svg viewBox="0 0 90 90"><circle cx="45" cy="45" r="40" fill="none" stroke="#eef3cc" stroke-width="7"/><circle cx="45" cy="45" r="40" fill="none" stroke="#bfd22f" stroke-width="7" stroke-dasharray="42.7 251.3" transform="rotate(-90 45 45)"/></svg>
        <p>Female share of non-agricultural wage employment is only 17%</p>
      </div>
      <div class="stat">
        <svg viewBox="0 0 90 90"><circle cx="45" cy="45" r="40" fill="none" stroke="#eef3cc" stroke-width="7"/><circle cx="45" cy="45" r="40" fill="none" stroke="#bfd22f" stroke-width="7" stroke-dasharray="34.9 251.3" transform="rotate(-90 45 45)"/></svg>
        <p>Participation of women in the workforce is only, 13.9% in the urban sector</p>
      </div>
      <div class="stat">
        <svg viewBox="0 0 90 90"><circle cx="45" cy="45" r="40" fill="none" stroke="#eef3cc" stroke-width="7"/><circle cx="45" cy="45" r="40" fill="none" stroke="#bfd22f" stroke-width="7" stroke-dasharray="75.1 251.3" transform="rotate(-90 45 45)"/></svg>
        <p>29.9% in the rural sector</p>
      </div>
      <div class="stat-box">Child Sex Ratio (0-6 years): The child sex ratio has dropped from 945 females per 1000 males in 1991 to 927 females per 1000 males in 2001</div>
    </div>
    <hr class="rule rule--solid">
    <h2 class="teal">What role can you play?</h2>
    <ul class="ticks">
      <li>Understand and empathise that:
        <ul>
          <li>Women are humans.</li>
          <li>Humans need money to live.</li>
          <li>Money is earned by working.</li>
          <li>Humans need work.</li>
        </ul>
      </li>
      <li>Understand inequality and equality</li>
      <li>Communicate</li>
      <li>Break down stereotypes</li>
      <li>Differentiate empowerment from misandry</li>
    </ul>
  </div>

  <div class="panel panel--where">
    <h2>Where are we?</h2>
    <ul class="ticks">
      <li>Women working in the group live in Delhi</li>
      <li>Some of working members of the group live in rural areas of U. P</li>
      <li>With NO permission to go out for work, they have to stay at home for the care of other family members, their children, elders, and to take care of chores of the home.</li>
    </ul>
    <hr class="rule">
    <h2>What are we achieving?</h2>
    <ul class="ticks">
      <li>Empowering women to:</li>
      <li>Freely live life with a sense of self-worth, respect and dignity</li>
      <li>Have complete control of their life, both within and outside of their home and workplace</li>
      <li>Make their own choices and decisions</li>
      <li>Have equal rights to participate in social, religious and public activities</li>
      <li>Have equal social status in the society</li>
      <li>Have equal rights for social and economic justice</li>
      <li>Determine financial and economic choices, get equal opportunity for education</li>
      <li>Get equal employment opportunity without any gender bias</li>
      <li>Get safe and comfortable working environment</li>
    </ul>
  </div>

  <div class="panel panel--how">
    <h2>How do we do it?</h2>
    <ul class="ticks">
      <li>Offer vocational training to members for various types of skills such as paper crafts, incense making, handicrafts, and jewellery making.</li>
      <li>Facilitate selling of handicrafts made by the women through fair trade.</li>
      <li>Provides workshop on various issues such as hygiene and women’s rights.</li>
    </ul>
    <hr class="rule rule--solid">
    <h2>Our impact so far</h2>
    <ul class="ticks">
      <li>Many women in various villages are skilled, confident, and self-reliant today.</li>
      <li>They are empowered women who make their own decisions, unfettered by social norms and gender stereotypes.</li>
      <li>The opportunity to work hard to earn their own living changed their lives</li>
    </ul>
    <hr class="rule rule--solid">
    <h2 class="orange">How can you help?</h2>
    <ul class="ticks help">
      <li>Sponsor vocational trainings for our women workers</li>
      <li>Scholarship for girls for their higher education</li>
      <li>Help us in networking by spreading the word about us</li>
      <li>Help us to increase our sales</li>
      <li>Give us an opportunity to make corporate gifts</li>
      <li>Donate tools for craft or stitching</li>
    </ul>
  </div>
</section>

</body>
</html>
```